Torvane Systems*

Stationary design including business cards, letter heads, envelops and email signatures using our new logo

Target Market(s)

Innovative Technologies

Industry/Entity Type

Defense Contracting

Font styles to use
Sans Serif

```html
<!DOCTYPE html>
<html lang="en">
<head>
<meta charset="utf-8">
<title>Torvane Systems Stationery</title>
<link rel="stylesheet" href="https://fonts.googleapis.com/css2?family=Source+Sans+3:wght@400;600&display=swap">
<style>
:root{
  --stage:#c6c6c6;
  --paper:#ffffff;
  --ink:#1e1e1e;
  --ink-deep:#000000;
  --text:#555555;
  --rule:#6a6a6a;
}
*{margin:0;padding:0;box-sizing:border-box}
html,body{width:1200px;height:820px;overflow:hidden}
body{background:var(--stage);font-family:"Source Sans 3",sans-serif;color:var(--text);position:relative}
.sheet{position:absolute;background:var(--paper);overflow:hidden}
.base-bar{position:absolute;left:0;right:0;bottom:0;background:var(--ink)}
.brand{position:absolute;display:flex;align-items:center;gap:6px;color:var(--ink-deep);font-weight:600;white-space:nowrap}
.brand-square{display:inline-block;border:1.5px solid var(--ink-deep)}
.divider{position:absolute;width:1px;background:var(--rule)}
.contact{position:absolute;line-height:1.3}
.contact .person{color:var(--ink);font-weight:600;line-height:1}
.contact .role{color:var(--text)}
.contact .line{display:flex;align-items:center;gap:4px;white-space:nowrap}
.icon{flex:none}

/* letterhead */
.letterhead{left:22px;top:64px;width:570px;height:718px}
.letterhead .base-bar{height:8px;left:2px}
.letterhead .brand{left:0;right:0;top:150px;justify-content:center;font-size:26px}
.letterhead .brand-square{width:14px;height:14px}
.letterhead .footer{position:absolute;left:0;right:0;top:679px;text-align:center;font-size:8.6px;line-height:14px}
.letterhead .footer .row{display:flex;justify-content:center;gap:14px}
.letterhead .footer .line{display:flex;align-items:center;gap:4px}

/* email signature */
.signature{left:634px;top:64px;width:475px;height:151px}
.signature .base-bar{height:7px}
.signature .brand{left:0;width:224px;top:106px;justify-content:center;font-size:22px}
.signature .brand-square{width:12px;height:12px}
.signature .divider{left:233px;top:21px;height:112px}
.signature .contact{left:259px;top:16px;font-size:9.4px}
.signature .person{font-size:21px}
.signature .role{font-size:11px;margin:3px 0 10px}
.signature .address{margin-bottom:6px;line-height:12px}
.signature .line{height:17px}

/* business card back */
.card-back{left:634px;top:269px;width:261px;height:140px;background:var(--ink)}
.card-back .brand{left:0;right:0;top:58px;justify-content:center;font-size:17px;color:var(--paper)}
.card-back .brand-square{width:10px;height:10px;border-color:var(--paper)}

/* business card front */
.card-front{left:909px;top:269px;width:261px;height:140px}
.card-front .base-bar{height:5px}
.card-front .brand{left:0;width:117px;top:92px;justify-content:center;font-size:12px}
.card-front .brand-square{width:7px;height:7px;border-width:1px}
.card-front .divider{left:117px;top:28px;height:95px}
.card-front .contact{left:132px;top:28px;font-size:7px}
.card-front .person{font-size:11.5px}
.card-front .role{font-size:7px;margin:2px 0 7px}
.card-front .address{margin-bottom:3px;line-height:9.5px}
.card-front .line{height:12px}

/* envelope */
.envelope{left:622px;top:486px;width:486px;height:295px;background:transparent}
.envelope .flap{position:absolute;left:0;top:0}
.envelope .body{position:absolute;left:0;top:64px;width:486px;height:231px;background:var(--paper)}
.envelope .base-bar{height:7px;bottom:1px}
.envelope .brand{left:10px;top:58px;font-size:17px}
.envelope .brand-square{width:10px;height:10px}
.envelope .divider{left:364px;top:16px;height:62px}
.envelope .contact{left:369px;top:16px;font-size:6.6px}
.envelope .address{margin-bottom:8px;line-height:8.5px}
.envelope .line{height:12.5px}
</style>
</head>
<body>

<svg width="0" height="0" style="position:absolute">
  <defs>
    <symbol id="i-phone" viewBox="0 0 16 16"><circle cx="8" cy="8" r="7" fill="none" stroke="#1e1e1e" stroke-width="1.4"/><path d="M5.3 4.3l1.6-.3.8 2-1 .8a5 5 0 0 0 2.5 2.5l.8-1 2 .8-.3 1.6c-3.6.3-6.7-2.8-6.4-6.4z" fill="#1e1e1e"/></symbol>
    <symbol id="i-mail" viewBox="0 0 16 12"><rect x="0" y="0" width="16" height="12" fill="#1e1e1e"/><path d="M0.5 0.8L8 7l7.5-6.2" fill="none" stroke="#fff" stroke-width="1.3"/></symbol>
    <symbol id="i-globe" viewBox="0 0 16 16"><g fill="none" stroke="#555" stroke-width="1.1"><circle cx="8" cy="8" r="7"/><ellipse cx="8" cy="8" rx="3" ry="7"/><path d="M1 8h14M2 4.5h12M2 11.5h12"/></g></symbol>
  </defs>
</svg>

<section class="sheet letterhead">
  <div class="brand"><span class="brand-square"></span>Torvane Systems</div>
  <div class="footer">
    <div>48 Harlow Ridge Rd., Suite 310, Westbrook Park, Halden County,</div>
    <div class="row">
      <span class="line"><svg class="icon" width="9" height="9"><use href="#i-phone"/></svg>+1 5550147283</span>
      <span class="line"><svg class="icon" width="8" height="6"><use href="#i-mail"/></svg>info@torvanesystems.com</span>
      <span class="line"><svg class="icon" width="8" height="8"><use href="#i-globe"/></svg>www.torvanesystems.com</span>
    </div>
  </div>
  <div class="base-bar"></div>
</section>

<section class="sheet signature">
  <div class="brand"><span class="brand-square"></span>Torvane Systems</div>
  <div class="divider"></div>
  <div class="contact">
    <div class="person">Daniel Mercer</div>
    <div class="role">CEO</div>
    <div class="address">48 Harlow Ridge Rd., Suite 310, Westbrook<br>Park, Halden County,</div>
    <div class="line"><svg class="icon" width="9" height="9"><use href="#i-phone"/></svg>+1 5550147283</div>
    <div class="line"><svg class="icon" width="8" height="6"><use href="#i-mail"/></svg>info@torvanesystems.com</div>
    <div class="line"><svg class="icon" width="8" height="8"><use href="#i-globe"/></svg>www.torvanesystems.com</div>
  </div>
  <div class="base-bar"></div>
</section>

<section class="sheet card-back">
  <div class="brand"><span class="brand-square"></span>Torvane Systems</div>
</section>

<section class="sheet card-front">
  <div class="brand"><span class="brand-square"></span>Torvane Systems</div>
  <div class="divider"></div>
  <div class="contact">
    <div class="person">Daniel Mercer</div>
    <div class="role">CEO</div>
    <div class="address">48 Harlow Ridge Rd., Suite<br>310, Westbrook Park,<br>Halden County,</div>
    <div class="line"><svg class="icon" width="8" height="8"><use href="#i-phone"/></svg>+1 5550147283</div>
    <div class="line"><svg class="icon" width="7" height="5"><use href="#i-mail"/></svg>info@torvanesystems.com</div>
    <div class="line"><svg class="icon" width="7" height="7"><use href="#i-globe"/></svg>www.torvanesystems.com</div>
  </div>
  <div class="base-bar"></div>
</section>

<section class="sheet envelope">
  <svg class="flap" width="486" height="65" viewBox="0 0 486 65">
    <path d="M0 64 L17 8 Q20 0 30 0 L456 0 Q466 0 469 8 L486 64 Z" fill="#000"/>
  </svg>
  <div class="body">
    <div class="brand"><span class="brand-square"></span>Torvane Systems</div>
    <div class="divider"></div>
    <div class="contact">
      <div class="address">48 Harlow Ridge Rd., Suite 310, West-<br>brook Park, Halden County,</div>
      <div class="line"><svg class="icon" width="6" height="6"><use href="#i-phone"/></svg>+1 5550147283</div>
      <div class="line"><svg class="icon" width="6" height="4"><use href="#i-mail"/></svg>info@torvanesystems.com</div>
      <div class="line"><svg class="icon" width="6" height="6"><use href="#i-globe"/></svg>www.torvanesystems.com</div>
    </div>
    <div class="base-bar"></div>
  </div>
</section>

</body>
</html>
```